Dental FAQ/advert tri-fold for holistic family dentist

We are a dental clinic with a holistic emphasis. We are seeking new clients, mainly middle classed families. A tri-fold brochure that is both a useful dental FAQ to keep in the house and acts as an advertisement for our clinic. It will be mailed out. It needs to look clean, modern, somewhat minimalist, and I want it to follow the Orble design esthetic. website is willowcrestdentalcare.com
Updates

I just updated the pamphlet file with revised text! Thanks for the nice designs so far, keep em coming.

Target Market(s)

Young families. Upper middle classes.

Industry/Entity Type

Dental

Requirements
Must have
• Follows our logo and colours.

```html
<!DOCTYPE html>
<html lang="en">
<head>
<meta charset="utf-8">
<title>Willowcrest Dental Care – FAQ Tri-fold</title>
<link rel="stylesheet" href="https://fonts.googleapis.com/css2?family=Open+Sans:wght@400;600;700&display=swap">
<style>
  :root{
    --blue:#2e5ea8;
    --blue-text:#2b55a0;
    --green:#3aa935;
    --green-light:#6cc04a;
    --paper:#ffffff;
    --paper-grey:#eef0f2;
    --ink:#1f2a38;
    --white:#ffffff;
    --photo-warm-a:#d9c7b5;
    --photo-warm-b:#f1e6da;
    --photo-fam-a:#5fae3e;
    --photo-fam-b:#e8eaec;
  }
  *{box-sizing:border-box;margin:0;padding:0}
  html,body{width:1200px;height:871px;overflow:hidden;background:#e4e6e8}
  body{font-family:"Open Sans",Arial,sans-serif;color:var(--ink)}
  .brochure{display:flex;width:1200px;height:871px}
  .panel{position:relative;width:400px;height:871px;overflow:hidden}

  /* Shared FAQ styles */
  .faq-list{position:absolute;left:34px;right:30px}
  .faq{margin-bottom:18px}
  .faq:last-child{margin-bottom:0}
  .faq__q{display:flex;gap:10px;align-items:flex-start;font-weight:700;font-size:16px;line-height:1.22;color:var(--blue-text);margin-bottom:5px}
  .faq__bullet{flex:none;width:11px;height:11px;margin-top:4px;border-radius:50%;background:var(--blue-text)}
  .faq__a{font-size:12px;line-height:1.45;font-weight:600;color:var(--ink)}

  /* Inside panel */
  .panel--faq-light{background:var(--paper)}
  .hero-photo{position:absolute;left:0;top:0;width:400px;height:260px;
    background:linear-gradient(135deg,var(--photo-warm-b),var(--photo-warm-a))}
  .swoosh{position:absolute;left:0;width:400px}
  .panel--faq-light .swoosh{top:180px;height:100px}
  .panel--faq-light .faq-list{top:290px}

  /* Middle panel */
  .panel--faq-blue{background:var(--blue)}
  .panel--faq-blue .faq-list{top:54px}
  .panel--faq-blue .faq{margin-bottom:20px}
  .panel--faq-blue .faq__q{color:var(--white)}
  .panel--faq-blue .faq__bullet{background:var(--green-light)}
  .panel--faq-blue .faq__a{color:#dfe7f4;font-weight:400}
  .contact{position:absolute;left:0;right:0;top:600px;text-align:center;color:var(--white)}
  .contact__location{font-size:16px;letter-spacing:.3px;margin-bottom:10px}
  .contact__phone{display:inline-block;background:var(--green);border:2px solid #fff;border-radius:8px;
    padding:6px 22px;font-size:24px;font-weight:700;letter-spacing:.5px}
  .contact__web{margin-top:18px;font-size:13px;line-height:1.5;color:#cfdaee}

  /* Cover */
  .panel--cover{background:var(--paper-grey)}
  .brand{position:absolute;left:0;right:0;top:58px;display:flex;align-items:center;justify-content:center;gap:10px}
  .brand__dot{width:18px;height:18px;border-radius:50%;background:var(--green)}
  .brand__name{font-weight:700;font-size:24px;color:var(--green)}
  .cover-title{position:absolute;right:44px;top:130px;text-align:right;font-weight:700;font-size:17px;line-height:1.3;color:var(--blue-text)}
  .cover-rule{position:absolute;right:40px;top:200px;width:190px;height:2px;background:var(--green)}
  .cover-photo{position:absolute;left:0;top:215px;width:400px;height:400px;
    background:radial-gradient(ellipse at 55% 55%,var(--photo-fam-a) 0%,#9ccf7e 45%,var(--photo-fam-b) 80%)}
  .panel--cover .swoosh{top:560px;height:311px}
  .cover-tagline{position:absolute;left:0;right:0;bottom:100px;text-align:center;color:var(--white);
    font-size:21px;letter-spacing:1px;line-height:1.35;text-transform:uppercase}
</style>
</head>
<body>
<main class="brochure">

  <section class="panel panel--faq-light">
    <div class="hero-photo" role="img" aria-label="Photo of a smiling young couple"></div>
    <svg class="swoosh" viewBox="0 0 400 100" preserveAspectRatio="none" aria-hidden="true">
      <path d="M0 72 C120 72 260 36 400 0 L400 100 L0 100Z" fill="var(--green)"/>
      <path d="M0 80 C120 80 260 48 400 14 L400 100 L0 100Z" fill="var(--blue)"/>
      <path d="M0 86 C120 86 260 58 400 24 L400 100 L0 100Z" fill="var(--paper)"/>
    </svg>
    <div class="faq-list">
      <article class="faq">
        <h3 class="faq__q"><span class="faq__bullet"></span>How can I manage my sensitive teeth?</h3>
        <p class="faq__a">Using a soft bristled toothbrush as well as desensitizing toothpaste is helpful, but many people still experience painful teeth sensitivity. We are pleased to offer effective laser desensitization, which is both gentle and painless. Other dental procedures that may help reduce sensitivity include using white fillings or applying dentin sealers to cover exposed root surfaces. Using a custom fit mouth guard can also prevent further enamel wear.</p>
      </article>
      <article class="faq">
        <h3 class="faq__q"><span class="faq__bullet"></span>Do I need to have my wisdom teeth removed?</h3>
        <p class="faq__a">While some people keep their wisdom teeth well into adulthood, wisdom teeth often do not grow in properly and need to be removed before a problem arises. This usually happens between the ages of 16-22. Our dentist will be able to assess your wisdom teeth and provide proper treatment.</p>
      </article>
      <article class="faq">
        <h3 class="faq__q"><span class="faq__bullet"></span>What can cause a toothache?</h3>
        <p class="faq__a">Toothaches are caused by an irritated nerve within the tooth, by or an infection surrounding the tooth. Prior to your dental appointment an over the counter pain medication such as ibuprofen will usually provide temporary relief. At your visit, our dentist will determine the exact cause of the problem and provide treatment options.</p>
      </article>
    </div>
  </section>

  <section class="panel panel--faq-blue">
    <div class="faq-list">
      <article class="faq">
        <h3 class="faq__q"><span class="faq__bullet"></span>What should I do if I knock a tooth out?</h3>
        <p class="faq__a">Say sorry to the other person! Just kidding. If a tooth is knocked clean out, it can sometimes be re-implanted, if done within 30-60 minutes. Gently rinse the tooth off, and store it in a solution of milk or clean water and make your way to a dentist as soon as possible.</p>
      </article>
      <article class="faq">
        <h3 class="faq__q"><span class="faq__bullet"></span>Should I wear a mouth guard during recreational activities?</h3>
        <p class="faq__a">Mouth guards should be used by anyone who plays contact sports such as hockey, football, boxing, soccer, basketball, and lacrosse. Your dentist can create a custom appliance that provides much more comfort and protection than a store-bought appliance.</p>
      </article>
      <article class="faq">
        <h3 class="faq__q"><span class="faq__bullet"></span>What’s the difference between teeth whitening in a dental office and store bought kits?</h3>
        <p class="faq__a">Our dental clinic can supply you with a custom fit tray to maximize your teeth whitening. Our dental office is able to prescribe stronger formulations of the whitening solution for a longer lasting, whiter smile.</p>
      </article>
    </div>
    <div class="contact">
      <p class="contact__location">located at Maple Ave. and Birch Rd.</p>
      <p class="contact__phone">Call us: (555) 014-2870</p>
      <p class="contact__web">See our website for a virtual tour of our clinic.<br>www.willowcrestdentalcare.com</p>
    </div>
  </section>

  <section class="panel panel--cover">
    <div class="brand"><span class="brand__dot"></span><span class="brand__name">Willowcrest Dental Care</span></div>
    <h2 class="cover-title">Frequently Asked<br>Questions For<br>Your Dentist</h2>
    <div class="cover-rule"></div>
    <div class="cover-photo" role="img" aria-label="Photo of a smiling family: father, mother and young son"></div>
    <svg class="swoosh" viewBox="0 0 400 311" preserveAspectRatio="none" aria-hidden="true">
      <path d="M0 110 C140 90 280 60 400 0 L400 311 L0 311Z" fill="var(--green)"/>
      <path d="M0 124 C140 104 280 76 400 18 L400 311 L0 311Z" fill="var(--paper)"/>
      <path d="M0 132 C140 112 280 86 400 30 L400 311 L0 311Z" fill="var(--blue)"/>
    </svg>
    <p class="cover-tagline">Providing dental care<br>for your whole family</p>
  </section>

</main>
</body>
</html>
```